Wag Without Worry Business cards

Design a cool, modern business card for my bully breed rescue.

Contact Information for Business Card

Mirela
512-384-2076 Mirela@WagWithoutWorry.net WagWithoutWorry.net

Font styles to use
Serif
Sans Serif

Colors

Designer to choose colors to be used in the design.

Requirements
Must have
• logo and info. Color
Nice to have
• Foil. Maybe some paw prints on the back or some kind of dog illustration.

```html
<!DOCTYPE html>
<html lang="en">
<head>
<meta charset="utf-8">
<title>Wag Without Worry – Business Cards</title>
<link rel="stylesheet" href="https://fonts.googleapis.com/css2?family=Montserrat:wght@400;800&family=Sacramento&display=swap">
<style>
  :root {
    --backdrop: #2a2a2a;
    --card: #1e1e1e;
    --card-edge: #272727;
    --foil: #d9d9d9;
    --foil-line: #8a8a8a;
    --gold: #f5c81f;
    --ink: #f0f0f0;
    --emboss-dark: #121212;
    --emboss-mid: #1a1a1a;
  }
  * { margin: 0; padding: 0; box-sizing: border-box; }
  html, body {
    width: 1200px;
    height: 900px;
    overflow: hidden;
    background: radial-gradient(ellipse at 60% 20%, #333 0%, var(--backdrop) 60%, #222 100%);
    font-family: "Montserrat", sans-serif;
  }
  .card {
    position: absolute;
    left: 230px;
    width: 740px;
    height: 405px;
    background: var(--card);
    border: 1px solid var(--card-edge);
    box-shadow: 0 20px 44px rgba(0,0,0,0.5);
    overflow: hidden;
  }
  .card--front { top: 30px; }
  .card--back { top: 465px; }

  .brand {
    position: absolute;
    inset: 0;
    display: flex;
    align-items: center;
    justify-content: center;
  }
  .brand__ring {
    position: absolute;
    left: 50%;
    top: 50%;
    width: 270px;
    height: 270px;
    margin: -135px 0 0 -135px;
    border: 2px solid var(--foil-line);
    border-radius: 50%;
  }
  .brand__name {
    position: relative;
    font-family: "Montserrat", sans-serif;
    font-weight: 800;
    font-size: 50px;
    color: var(--foil);
    text-transform: uppercase;
    letter-spacing: 1px;
    background: var(--card);
    padding: 4px 14px;
  }

  .dog-art {
    position: absolute;
    left: 0;
    top: 10px;
    width: 330px;
    height: 395px;
    background:
      radial-gradient(ellipse at 55% 40%, var(--emboss-mid) 0%, var(--emboss-dark) 80%);
    border-radius: 30% 52% 38% 0 / 18% 40% 55% 0;
    box-shadow:
      inset 2px 2px 0 rgba(255,255,255,0.06),
      inset -3px -3px 6px rgba(0,0,0,0.6),
      1px 1px 0 rgba(255,255,255,0.05);
  }

  .contact {
    position: absolute;
    right: 60px;
    top: 70px;
    text-align: right;
    color: var(--ink);
  }
  .contact__name {
    font-family: "Sacramento", cursive;
    font-size: 104px;
    color: var(--gold);
    line-height: 1;
    margin-bottom: 26px;
    margin-right: -8px;
  }
  .contact__line {
    font-size: 23px;
    font-weight: 400;
    line-height: 1.55;
    letter-spacing: 0.5px;
  }
</style>
</head>
<body>
  <section class="card card--front" aria-label="Card front">
    <div class="brand">
      <span class="brand__ring"></span>
      <span class="brand__name">Wag Without Worry</span>
    </div>
  </section>

  <section class="card card--back" aria-label="Card back">
    <div class="dog-art" role="img" aria-label="Large embossed black line illustration of a bully breed dog's head"></div>
    <div class="contact">
      <p class="contact__name">Mirela</p>
      <p class="contact__line">512·384·2076</p>
      <p class="contact__line">Mirela@WagWithoutWorry.net</p>
      <p class="contact__line">WagWithoutWorry.net</p>
    </div>
  </section>
</body>
</html>
```